Lift Your Standing - Search Engine Website

I am launching an SEO website and I am looking to have the site designed. There are a total of 8-10 pages that will need to be designed. I am providing 2 pages off the bat and will work with a designer once these 2 pages are complete. I have never posted a contest for website design (only logos, brochures, etc) so please let me know if there is anything you need from me. I am uploading 2 versions of our logo - a horizontal and a vertical version. I was thinking of getting these rendered in 3d, but I am just going with these for now. I am hoping to complete all work in 10 days, so hopefully the right design for the 1st 2 pages are submitted promptly.

We provide search engine optomization tools and backlinking tools. We provide free research tools as well as cost effective packages for SEO.

I am including 2 word files that have info about the home page and keyword summary page. Additional pages will include: Keyword Research Summary, The Slate, Reports, etc.

I am also uploading a zip file that has some examples of home pages that I like. None of them are exactly what I am looking for, but they have certain elements that I like.

I am looking for a clean design and stands out and has good use of color.

Link to instructions files (2...more will be uploaded as first 2 pages are finalized): https://www.filecrate-example.net/sh/k4m2w7z9q3v1b8x/tRn_p-7ab2
Updates

Forgot to include our logos. Here is a drop box link to the logos: 

https://www.filecrate-example.net/sh/93jd2kq7zt5wmvp/8h2PLmz4Xe

Target Market(s)

big and small businesses, resellers

Industry/Entity Type

Seo

Requirements
Must have
• see attached MS Word files for details about requirements.

```html
<!DOCTYPE html>
<html lang="en">
<head>
<meta charset="utf-8">
<title>Lift Your Standing – Search Engine Rankings</title>
<link href="https://fonts.googleapis.com/css2?family=Arimo:wght@400;700&display=swap" rel="stylesheet">
<style>
:root{
  --blue:#1c7fd0;
  --blue-dark:#125fa6;
  --blue-deep:#0c4c86;
  --navy:#0a3766;
  --orange:#f7941d;
  --orange-dark:#e2780a;
  --green:#5cb531;
  --green-dark:#46961f;
  --ink:#3c4650;
  --muted:#7a8590;
  --line:#dfe5eb;
  --soft:#eef2f6;
  --white:#ffffff;
}
*{box-sizing:border-box;margin:0;padding:0}
html,body{width:818px;height:1200px;overflow:hidden}
body{position:relative;background:var(--white);font-family:"Arimo",Arial,sans-serif;color:var(--ink);font-size:8px;line-height:1.35}
.abs{position:absolute}

/* header */
.brand{left:150px;top:12px;display:flex;align-items:center;gap:7px;font-size:20px;font-weight:700;color:var(--blue);letter-spacing:-.3px}
.brand-dot{width:14px;height:14px;border-radius:50%;background:var(--orange)}
.top-actions{right:142px;top:10px;display:flex;gap:6px}
.top-btn{height:16px;padding:0 9px;border-radius:2px;font-size:7.5px;line-height:16px;color:var(--white);background:var(--blue-dark)}
.top-btn.alt{background:var(--orange)}

.main-nav{left:144px;top:52px;width:530px;height:22px;background:linear-gradient(var(--blue),var(--blue-dark));display:flex;align-items:center}
.main-nav span{color:var(--white);font-size:8px;padding:0 8px;border-right:1px solid rgba(255,255,255,.25);line-height:22px}
.main-nav .signup{margin-left:auto;background:var(--orange);border:0;font-weight:700;padding:0 14px}

.member-bar{left:0;top:74px;width:818px;height:16px;background:var(--soft);border-bottom:1px solid var(--line)}
.member-bar ul{list-style:none;position:absolute;left:150px;top:0;display:flex;gap:12px;line-height:16px;font-size:7px;color:var(--muted)}
.member-bar li:first-child{color:var(--blue-dark);font-weight:700}

/* hero */
.hero{left:0;top:90px;width:818px;height:235px;background:linear-gradient(180deg,#2a94dc 0%,var(--blue) 45%,var(--blue-dark) 100%)}
.hero-title{left:158px;top:102px;width:376px;font-size:13px;font-weight:700;color:var(--white);white-space:nowrap;overflow:hidden}
.hero-points{left:158px;top:124px;list-style:none;color:var(--white);font-size:7.5px}
.hero-points li{display:flex;align-items:center;gap:5px;margin-bottom:3px}
.tick{width:9px;height:9px;border-radius:50%;background:var(--green);display:inline-block;position:relative}
.tick:after{content:"";position:absolute;left:3px;top:1.5px;width:2px;height:4px;border:solid #fff;border-width:0 1.2px 1.2px 0;transform:rotate(45deg)}
.laptop{left:168px;top:165px;width:158px;height:140px;border-radius:4px;background:linear-gradient(160deg,#dfe9f3,#9fb6cc 70%,#6d849b)}

.keyword-box{left:336px;top:182px;width:196px;height:120px}
.keyword-head{display:flex;align-items:center;gap:6px;color:var(--white);font-size:17px;font-weight:700}
.field{height:18px;margin-top:7px;border-radius:2px;background:var(--white);color:#9aa4ad;font-size:7.5px;line-height:18px;padding:0 7px}
.field-row{display:flex;gap:6px}
.field-row .field{flex:1}
.caret{float:right;color:var(--muted)}
.search-btn{left:582px;top:282px;width:86px;height:20px;border-radius:3px;background:linear-gradient(var(--orange),var(--orange-dark));color:var(--white);font-size:9px;font-weight:700;text-align:center;line-height:20px}

.signup-panel{left:540px;top:74px;width:134px;height:188px;background:var(--orange);padding:8px 9px;box-shadow:0 3px 6px rgba(0,0,0,.25)}
.signup-panel .input{height:14px;background:var(--white);border-radius:2px;margin-bottom:4px;font-size:6.5px;line-height:14px;padding:0 5px;color:#9aa4ad}
.agree{display:flex;gap:4px;align-items:flex-start;font-size:6px;color:var(--white);margin:4px 0 5px}
.agree i{width:7px;height:7px;background:var(--white);flex:none;margin-top:1px}
.register{width:44px;height:14px;margin-left:auto;margin-right:auto;background:var(--blue-dark);color:var(--white);border-radius:2px;font-size:7px;text-align:center;line-height:14px}

.hero-note{left:478px;top:331px;width:190px;font-size:7px;color:var(--muted)}

/* calls to action */
.cta{top:390px;height:38px;border-radius:4px;color:var(--white);font-size:17px;font-weight:700;display:flex;align-items:center;justify-content:center;gap:8px}
.cta.buy{left:156px;width:138px;background:linear-gradient(var(--green),var(--green-dark))}
.cta.trial{left:300px;width:138px;background:linear-gradient(var(--orange),var(--orange-dark))}
.trial-days{left:450px;top:400px;font-size:15px;font-weight:700;color:var(--ink);display:flex;align-items:center;gap:6px}

/* features */
.features{left:156px;top:458px;width:520px;display:grid;grid-template-columns:repeat(3,1fr);column-gap:18px;row-gap:16px}
.feature{display:flex;gap:7px}
.feature-icon{flex:none;width:22px;height:22px;border-radius:50%;background:var(--orange);display:flex;align-items:center;justify-content:center}
.feature h3{font-size:9px;color:var(--blue-dark);margin:3px 0 4px}
.feature p{font-size:6.8px;color:var(--muted)}

.divider{left:144px;top:700px;width:530px;height:1px;background:var(--line)}

/* media + blog */
.video{left:158px;top:742px;width:330px;height:220px;background:#111;border:1px solid #333}
.video-frame{position:absolute;left:0;top:0;width:100%;height:198px;background:radial-gradient(circle at 50% 45%,#3a3f45,#0c0d0f 70%)}
.play{position:absolute;left:145px;top:79px}
.video-bar{position:absolute;left:0;bottom:0;width:100%;height:22px;background:#1d1f22;display:flex;align-items:center;gap:8px;padding:0 8px}
.progress{flex:1;height:3px;background:#444}
.progress b{display:block;width:18%;height:100%;background:#bbb}
.video-time{color:#bbb;font-size:6.5px}

.blog-title{left:510px;top:736px;font-size:16px;font-weight:700;color:var(--ink)}
.blog-title span{color:var(--orange)}
.blog-list{left:510px;top:770px;width:166px;list-style:none}
.blog-list li{display:flex;gap:7px;margin-bottom:14px;height:36px}
.date{flex:none;width:28px;height:30px;background:var(--blue);color:var(--white);text-align:center;font-size:10px;font-weight:700;line-height:1;padding-top:5px;border-radius:2px}
.date small{display:block;font-size:6px;font-weight:400;margin-top:2px}
.blog-list p{font-size:6.6px;color:var(--muted)}
.blog-list a{display:block;color:var(--blue-dark);font-size:6.6px;text-decoration:none;margin-top:1px}

/* footer */
.footer{left:0;top:992px;width:818px;height:183px;background:linear-gradient(var(--blue-deep),#0b4379)}
.footer-col{top:1012px;color:#cfe0f0;font-size:7px}
.footer-col h4{color:var(--white);font-size:9px;margin-bottom:7px}
.footer-col li{list-style:none;margin-bottom:4px}
.footer-brand{left:560px;top:1050px;display:flex;align-items:center;gap:6px;font-size:16px;font-weight:700;color:var(--white)}
.footer-brand .brand-dot{width:12px;height:12px}
.footer-base{left:0;top:1175px;width:818px;height:25px;background:var(--navy)}
.copyright{left:150px;top:1184px;font-size:6.5px;color:#9fb8d0}
.social{right:142px;top:1181px;display:flex;gap:6px}
.social i{width:12px;height:12px;background:#2e6aa6;border-radius:2px}
</style>
</head>
<body>

<header>
  <div class="abs brand"><span class="brand-dot"></span>Lift Your Standing</div>
  <div class="abs top-actions">
    <span class="top-btn">Like Our Page</span>
    <span class="top-btn alt">Tell a Friend</span>
  </div>
  <nav class="abs main-nav">
    <span>Home</span><span>About Us</span><span>Services ▾</span><span>Features ▾</span><span>Resources ▾</span><span>Free Trial</span><span>FAQ</span><span>Blog</span><span>Contact Us</span><span class="signup">Sign Up</span>
  </nav>
  <div class="abs member-bar">
    <ul>
      <li>Members Area</li><li>My Account</li><li>Edit My Profile</li><li>My Order History</li><li>Tutorials</li><li>Saved Keywords</li><li>Ranking Report</li><li>Log Out</li>
    </ul>
  </div>
</header>

<section>
  <div class="abs hero"></div>
  <h1 class="abs hero-title">Boost Your Search Engine Rankings Using Legal Back Links</h1>
  <ul class="abs hero-points">
    <li><span class="tick"></span>Rapid Rankings of your Business Webpage, Video Channel, Social Media Page &amp; Blog</li>
    <li><span class="tick"></span>Report Pages from across our network</li>
  </ul>
  <div class="abs laptop" role="img" aria-label="Laptop showing colourful ranking charts"></div>

  <div class="abs keyword-box">
    <div class="keyword-head">
      <svg width="16" height="16" viewBox="0 0 16 16"><circle cx="6.5" cy="6.5" r="4.8" fill="none" stroke="#fff" stroke-width="2"/><line x1="10" y1="10" x2="14.5" y2="14.5" stroke="#fff" stroke-width="2.4" stroke-linecap="round"/></svg>
      Free Keyword
    </div>
    <div class="field">Enter Your Keyword</div>
    <div class="field">Enter Your Current Website URL</div>
    <div class="field-row">
      <div class="field">Search Engine <span class="caret">▾</span></div>
      <div class="field">Country <span class="caret">▾</span></div>
    </div>
  </div>
  <div class="abs search-btn">SEARCH</div>

  <form class="abs signup-panel">
    <div class="input">Full Name</div>
    <div class="input">Email Address</div>
    <div class="input">Phone Number</div>
    <div class="input">Choose a password</div>
    <div class="input">Confirm Password</div>
    <div class="input">Zip code</div>
    <div class="agree"><i></i>I agree to the Terms of Service and Privacy Policy</div>
    <div class="register">Register</div>
  </form>

  <p class="abs hero-note">Submit Your Current Search Engine Ranking, Research Keyword popularities and competitiveness. See what your competitors are doing!</p>
</section>

<section>
  <div class="abs cta buy">Buy Now
    <svg width="14" height="14" viewBox="0 0 14 14"><path d="M2 7h9M7 3l4 4-4 4" fill="none" stroke="#fff" stroke-width="2"/></svg>
  </div>
  <div class="abs cta trial">Free Trial</div>
  <div class="abs trial-days">
    <svg width="16" height="10" viewBox="0 0 16 10"><path d="M1 5h12M9 1l4 4-4 4" fill="none" stroke="#3c4650" stroke-width="2"/></svg>
    30 days
  </div>
</section>

<section class="abs features">
  <div class="feature"><span class="feature-icon"><svg width="10" height="10" viewBox="0 0 10 10"><path d="M2 5l2 2 4-4" fill="none" stroke="#fff" stroke-width="1.6"/></svg></span><div><h3>Free Trial</h3><p>Try every research tool at no cost for thirty days and see how your pages climb the results.</p></div></div>
  <div class="feature"><span class="feature-icon"><svg width="10" height="10" viewBox="0 0 10 10"><path d="M2 5l2 2 4-4" fill="none" stroke="#fff" stroke-width="1.6"/></svg></span><div><h3>SEO Tips</h3><p>Simple advice on titles, content and links that helps search engines understand your site better.</p></div></div>
  <div class="feature"><span class="feature-icon"><svg width="10" height="10" viewBox="0 0 10 10"><path d="M2 5l2 2 4-4" fill="none" stroke="#fff" stroke-width="1.6"/></svg></span><div><h3>What To Expect</h3><p>Clear reports, steady progress and honest timelines for every keyword you choose to track.</p></div></div>
  <div class="feature"><span class="feature-icon"><svg width="10" height="10" viewBox="0 0 10 10"><path d="M2 5l2 2 4-4" fill="none" stroke="#fff" stroke-width="1.6"/></svg></span><div><h3>Why Lift Your Standing?</h3><p>Legal back links, fair pricing and tools built for both small shops and large businesses.</p></div></div>
  <div class="feature"><span class="feature-icon"><svg width="10" height="10" viewBox="0 0 10 10"><path d="M2 5l2 2 4-4" fill="none" stroke="#fff" stroke-width="1.6"/></svg></span><div><h3>Tips To Using Our System</h3><p>Short guides show how to add keywords, read reports and plan your next campaign step.</p></div></div>
  <div class="feature"><span class="feature-icon"><svg width="10" height="10" viewBox="0 0 10 10"><path d="M2 5l2 2 4-4" fill="none" stroke="#fff" stroke-width="1.6"/></svg></span><div><h3>White Label</h3><p>Resellers can brand every report with their own name and share results with clients.</p></div></div>
  <div class="feature"><span class="feature-icon"><svg width="10" height="10" viewBox="0 0 10 10"><path d="M2 5l2 2 4-4" fill="none" stroke="#fff" stroke-width="1.6"/></svg></span><div><h3>SEO Basics</h3><p>Learn how rankings work, why links matter and which pages deserve your attention first.</p></div></div>
  <div class="feature"><span class="feature-icon"><svg width="10" height="10" viewBox="0 0 10 10"><path d="M2 5l2 2 4-4" fill="none" stroke="#fff" stroke-width="1.6"/></svg></span><div><h3>Free Keyword Analysis Tools</h3><p>Check search volume, competition and current position for any phrase in a few seconds.</p></div></div>
</section>

<div class="abs divider"></div>

<section>
  <div class="abs video">
    <div class="video-frame" role="img" aria-label="Introductory video still with the company name"></div>
    <svg class="play" width="40" height="40" viewBox="0 0 40 40"><circle cx="20" cy="20" r="19" fill="rgba(0,0,0,.55)" stroke="#fff" stroke-width="1.5"/><path d="M15 11l14 9-14 9z" fill="#fff"/></svg>
    <div class="video-bar">
      <svg width="8" height="9" viewBox="0 0 8 9"><path d="M0 0l8 4.5-8 4.5z" fill="#ccc"/></svg>
      <div class="progress"><b></b></div>
      <span class="video-time">00:00 / 02:14</span>
    </div>
  </div>

  <h2 class="abs blog-title">Recent from <span>Blog</span></h2>
  <ul class="abs blog-list">
    <li><div class="date">12<small>MAR</small></div><div><p>How fresh back links can move a local business page up the results in weeks.</p><a>Read more</a></div></li>
    <li><div class="date">08<small>MAR</small></div><div><p>Five keyword research habits that save time and bring steadier search traffic.</p><a>Read more</a></div></li>
    <li><div class="date">03<small>MAR</small></div><div><p>Why video pages rank well and how to give them the links they need.</p><a>Read more</a></div></li>
    <li><div class="date">27<small>FEB</small></div><div><p>A simple monthly report routine for resellers who manage many client sites.</p><a>Read more</a></div></li>
  </ul>
</section>

<footer>
  <div class="abs footer"></div>
  <div class="abs footer-col" style="left:158px"><h4>Company</h4><ul><li>About Us</li><li>Our Team</li><li>Careers</li><li>Contact Us</li><li>Privacy Policy</li></ul></div>
  <div class="abs footer-col" style="left:262px"><h4>Services</h4><ul><li>Back Links</li><li>Rank Tracking</li><li>White Label</li><li>Free Trial</li><li>Packages</li></ul></div>
  <div class="abs footer-col" style="left:360px"><h4>SEO</h4><ul><li>SEO Basics</li><li>SEO Tips</li><li>Keyword Tools</li><li>The Slate</li><li>Reports</li></ul></div>
  <div class="abs footer-col" style="left:455px"><ul><li>info@liftyourstanding.example</li><li>+1 (555) 014-2290</li></ul></div>
  <div class="abs footer-brand"><span class="brand-dot"></span>Lift Your Standing</div>
  <div class="abs footer-base"></div>
  <p class="abs copyright">© 2013 Lift Your Standing. All rights reserved.</p>
  <div class="abs social"><i></i><i></i></div>
</footer>

</body>
</html>
```